Chemical Distribution Company Needs a Website

We need a website designed for an existing company based in Michigan. We have grown substantially since inception and we need our website to reflect this growth. It currently has a very mom and pop feel to it. What we do is ship chemicals in Drums, Totes, Bags, Bulk Tank Trucks, and rail from our warehouses in Toledo Oh, and Chicago il. This will be a site that strictly shows what we do and will not be E-commerced based. The final design should communicate a large business with NorthAmerican reach and worldwide sourcing capabilities.

Target Market(s)

What we sell are chemicals such as acids, solvents, oils, and salts all of which are used in the manufacturing process of various products from steel to car parts to paint to car wash soaps to food. We are trying to look like a large company that has stability and track record to go after all types of industries and manufacturers

Industry/Entity Type

It Company

Number of Pages Required

5+ page

Font styles to use
Serif
Sans Serif

Requirements
Must have
• Be Formatted for WIX as that is what we use to Host and Build. Unless you have a better idea. I would also like it to be viewed on a mobile platform which it is not now.
• Tabs for:
• Home Page (similar to "www.brindlemoor.com")
• Who we are- with subtabs for (Overview, Leadership, and Capabilities)
• Chemicals- (subtabs for (overview, Chemicals A-Z) Look at Brindlemoor.com
• Metal Working Lubricants (with a drop down identical to the products tab at "www.veltraslube.com"
• Contact- Very similar to www.quorvanta.com/contact/
• Need to have professional photos of Chemical Facilities, Bulk Tanks Trucks, Chemical Railcars, Storage Facilities filled with Drums and Totes, a Tank Farm.
Nice to have
• Want to have our site look like a combination of quorvanta.com, brindlemoor.com, and plimtoreach.com

```html
<!DOCTYPE html>
<html lang="en">
<head>
<meta charset="utf-8">
<title>Kestrel Chemicals</title>
<link href="https://fonts.googleapis.com/css2?family=Roboto:wght@300;400;500;700&family=Oswald:wght@300;400&display=swap" rel="stylesheet">
<style>
  :root{
    --navy:#0b4068;
    --blue:#2196d9;
    --link:#1d5d96;
    --ink:#2b2b2b;
    --muted:#6e6e6e;
    --white:#ffffff;
    --page:#ffffff;
  }
  *{box-sizing:border-box;margin:0;padding:0}
  html,body{width:1200px;height:1070px;overflow:hidden;background:var(--page);font-family:"Roboto",sans-serif;color:var(--ink)}
  .canvas{position:relative;width:1200px;height:1070px}

  .topbar{position:absolute;top:0;left:0;width:1200px;height:42px;background:var(--navy);color:var(--white);font-size:15px}
  .topbar .contact{position:absolute;left:90px;top:12px;display:flex;gap:40px;align-items:center}
  .topbar .contact span{display:flex;align-items:center;gap:7px}
  .topbar .social{position:absolute;right:90px;top:14px;display:flex;gap:8px}
  .topbar .social i{display:block;width:15px;height:15px;background:var(--white);border-radius:3px}

  .header{position:absolute;top:42px;left:0;width:1200px;height:118px;background:var(--white)}
  .brand{position:absolute;left:90px;top:34px;height:56px;display:flex;align-items:center;gap:14px}
  .brand .mark{width:52px;height:52px;border-radius:50%;background:var(--blue)}
  .brand .name{font-size:25px;font-weight:700;color:var(--blue);letter-spacing:.4px;line-height:1}
  .nav{position:absolute;right:88px;top:52px;display:flex;gap:35px;font-size:15px}
  .nav a{color:var(--ink);text-decoration:none}
  .nav a.active{color:var(--blue)}

  .hero{position:absolute;top:160px;left:0;width:1200px;height:544px;background:linear-gradient(115deg,#cfd3d6 0%,#9aa1a6 35%,#7e868b 60%,#b5babd 100%)}
  .hero h1{position:absolute;left:0;width:1200px;top:248px;text-align:center;font-family:"Oswald",sans-serif;font-weight:400;font-size:64px;color:var(--white);letter-spacing:-1px;text-shadow:0 2px 4px rgba(0,0,0,.35)}
  .hero p{position:absolute;left:0;width:1200px;top:330px;text-align:center;font-family:"Oswald",sans-serif;font-weight:300;font-size:30px;color:var(--white);text-shadow:0 2px 4px rgba(0,0,0,.35)}
  .arrow{position:absolute;top:245px;width:28px;height:28px;border-radius:50%;background:rgba(0,0,0,.6)}
  .arrow.prev{left:69px}.arrow.next{right:69px}
  .arrow svg{position:absolute;left:8px;top:7px}

  .services{position:absolute;top:626px;left:88px;width:1024px;height:324px;background:var(--white);box-shadow:0 0 6px rgba(0,0,0,.2);padding:24px 20px 0 20px;display:grid;grid-template-columns:repeat(4,234px);column-gap:14px}
  .service .thumb{width:238px;height:154px;border:1px solid #e2e2e2;padding:3px;background:var(--white)}
  .service .thumb div{width:100%;height:100%}
  .service h2{font-size:14px;font-weight:400;margin-top:20px;letter-spacing:.2px}
  .service p{font-size:11px;color:var(--muted);line-height:19px;margin-top:9px;letter-spacing:.2px}
  .service a{display:block;font-size:11px;color:var(--link);text-decoration:none;margin-top:6px}

  .footer{position:absolute;top:950px;left:0;width:1200px;height:120px;background:var(--navy);color:var(--white);font-size:14px}
  .footer .links{position:absolute;left:90px;top:42px}
  .footer .links span{margin:0 8px}
  .footer .copy{position:absolute;left:91px;top:69px}
  .footer .social{position:absolute;right:90px;top:49px;display:flex;gap:10px}
  .footer .social i{display:block;width:34px;height:34px}
</style>
</head>
<body>
<div class="canvas">
  <div class="topbar">
    <div class="contact">
      <span><svg width="12" height="12" viewBox="0 0 12 12"><rect width="12" height="12" rx="2" fill="#fff"/><path d="M3.5 3c.5 2.5 2 4.5 5 5.5l.8-1.2-1.3-.8-.6.6C6.3 6.6 5.4 5.7 4.9 4.6l.6-.6-.8-1.3z" fill="#0b4068"/></svg>555-201-7384</span>
      <span><svg width="15" height="11" viewBox="0 0 15 11"><rect width="15" height="11" rx="1" fill="#fff"/><path d="M1 1l6.5 5L14 1" stroke="#0b4068" stroke-width="1.3" fill="none"/></svg>hello@kestrelchem.com</span>
    </div>
    <div class="social"><i></i><i></i><i></i><i></i></div>
  </div>

  <header class="header">
    <div class="brand">
      <div class="mark"></div>
      <div class="name">KESTREL CHEMICALS</div>
    </div>
    <nav class="nav">
      <a class="active" href="#">HOME</a>
      <a href="#">WHO WE ARE</a>
      <a href="#">CHEMICALS</a>
      <a href="#">METAL WORKING LUBRICANTS</a>
      <a href="#">CONTACT</a>
    </nav>
  </header>

  <section class="hero" role="img" aria-label="Photo of a chemical facility interior with steel tanks and a technician">
    <h1>CHEMICAL FACILITIES</h1>
    <p>NEQUE PORRO QUISQUAM EST QUI DOLOREM</p>
    <span class="arrow prev"><svg width="12" height="14" viewBox="0 0 12 14"><path d="M8 1L3 7l5 6" stroke="#fff" stroke-width="2" fill="none"/></svg></span>
    <span class="arrow next"><svg width="12" height="14" viewBox="0 0 12 14"><path d="M4 1l5 6-5 6" stroke="#fff" stroke-width="2" fill="none"/></svg></span>
  </section>

  <section class="services">
    <article class="service">
      <div class="thumb"><div role="img" aria-label="Photo of a chemical plant lit at dusk" style="background:linear-gradient(160deg,#3a3f6e,#b88a3a 60%,#2a2c44)"></div></div>
      <h2>CHEMICALS</h2>
      <p>Lorem Ipsum has been the industry's stan-<br>dard dummy text ever since the 1500s,</p>
      <a href="#">Read More &gt;&gt;</a>
    </article>
    <article class="service">
      <div class="thumb"><div role="img" aria-label="Photo of a bulk tank truck beside storage tanks" style="background:linear-gradient(180deg,#4f86c6,#c9d3dc 55%,#6b6e70)"></div></div>
      <h2>METAL WORKING LUBRICANTS</h2>
      <p>Lorem Ipsum has been the industry's stan-<br>dard dummy text ever since the 1500s,</p>
      <a href="#">Read More &gt;&gt;</a>
    </article>
    <article class="service">
      <div class="thumb"><div role="img" aria-label="Photo of storage silos by a green field" style="background:linear-gradient(180deg,#dfe4e8,#a9adb0 65%,#6f8f3a)"></div></div>
      <h2>CHEMICAL RAILCARS</h2>
      <p>Lorem Ipsum has been the industry's stan-<br>dard dummy text ever since the 1500s,</p>
      <a href="#">Read More &gt;&gt;</a>
    </article>
    <article class="service">
      <div class="thumb"><div role="img" aria-label="Photo of a refinery lit at night" style="background:linear-gradient(180deg,#2a5fb0,#3d4f8a 55%,#c99a4a)"></div></div>
      <h2>BULK TANKS TRUCKS</h2>
      <p>Lorem Ipsum has been the industry's stan-<br>dard dummy text ever since the 1500s,</p>
      <a href="#">Read More &gt;&gt;</a>
    </article>
  </section>

  <footer class="footer">
    <div class="links">Privacy Policy<span>|</span>Terms of Use<span>|</span>About Us<span>|</span>Sitemap</div>
    <div class="copy">Copyright © 2016&nbsp; All Rights</div>
    <div class="social">
      <i style="background:#29a9e1"></i>
      <i style="background:#d0271e"></i>
      <i style="background:#3b5998"></i>
      <i style="background:#0e76a8"></i>
    </div>
  </footer>
</div>
</body>
</html>
```